EmberGuard Larkton- Making Larkton A Wildfire Adapted Community

Design a two complimentary graphics with text that can be used for a banner and "mini-billboard" to promote the project and encourage citizens to go to the webpage to learn more. Using the attached document as examples of what we want the two banners to say.
The goal of EmberGuard Larkton is to plan and prepare so if an urban wildfire occurs, catastrophic loss can be avoided. EmberGuard Larkton focuses on reducing the risk of and catastrophic losses to resources and private property on private land in Larkton, MT. Property owners are encouraged to be proactive to address hazardous fuel conditions on their property, reduce structure ignition potential within their home ignition zone and employ wildfire resilient principles to sustain a fire adapted home, property and community. Ember showers from a wildfire next to the city is the biggest concern.

Target Market(s)

Residents in the project area of Larkton. Signs and banners will be displayed on public lands and private yeards

Font styles to use
Sans Serif

Requirements
Must have
• Graphics, use of the ValleyRidge Ember Watch Council logo. Must incorporate the text that is part of the attachment.
Nice to have
• Get people's attention. A simple graphic that get's people's attention.
Should not have
• small details.

```html
<!DOCTYPE html>
<html lang="en">
<head>
<meta charset="utf-8">
<title>EmberGuard Larkton – Wildfire Banners</title>
<link rel="stylesheet" href="https://fonts.googleapis.com/css2?family=Anton&family=Roboto:ital,wght@1,700;1,900&display=swap">
<style>
  :root{
    --red:#e8323a;
    --red-deep:#c9262e;
    --yellow:#fdc82a;
    --white:#ffffff;
    --ink:#141414;
    --green:#1f4a3a;
    --paper:#f4f4f4;
    --stage:#ececec;
  }
  *{box-sizing:border-box;margin:0;padding:0}
  html,body{width:1200px;height:1200px;overflow:hidden}
  body{
    background:var(--stage);
    font-family:"Anton",sans-serif;
    display:flex;justify-content:center;align-items:center;gap:80px;
  }
  .banner{
    width:360px;height:1060px;
    background:var(--paper);
    border:3px solid #d3d3d3;
    display:flex;flex-direction:column;
    box-shadow:0 4px 14px rgba(0,0,0,.12);
  }
  .red-block{
    background:var(--red);
    color:var(--white);
    text-align:center;
    display:flex;flex-direction:column;justify-content:center;align-items:center;
    text-shadow:2px 3px 4px rgba(0,0,0,.35);
    line-height:1.05;
  }
  .hl{color:var(--yellow)}

  /* Left banner */
  .hook{height:324px;padding:10px 12px}
  .hook .small{font-size:34px}
  .hook .big{font-size:66px;line-height:1.05}
  .hook .wild{font-size:60px}
  .scene-art{
    margin:6px 8px;height:180px;
    background:linear-gradient(180deg,#efe6b8 0%,#f2a94a 45%,#8bb24a 75%,#2f8a4a 100%);
  }
  .call{height:166px;margin-top:4px}
  .call span{font-size:66px;line-height:1.08;text-shadow:none}
  .choices{display:flex;flex-direction:column;align-items:center;gap:10px;padding:14px 0 6px}
  .pill{
    font-size:38px;line-height:1;padding:7px 18px 8px;border-radius:12px;
    background:var(--yellow);color:var(--ink);
  }
  .pill.loss{background:var(--red);color:var(--white)}

  /* Right banner */
  .promise{height:472px;padding:20px 14px;line-height:1.12}
  .promise .line{font-size:36px}
  .promise .key{font-size:52px;line-height:1.05}
  .promise .key small{font-size:36px;color:var(--white)}
  .home-art{
    height:190px;margin-top:12px;
    background:linear-gradient(180deg,#f4f4f4 0%,#e8323a 30%,#b52a2f 55%,#1a1a1a 100%);
  }
  .advice{
    text-align:center;color:var(--ink);font-size:35px;line-height:1.2;
    padding:22px 8px 0;
  }

  /* Shared footer */
  .footer{margin-top:auto;padding-bottom:22px;text-align:center}
  .learn{
    font-family:"Roboto",sans-serif;font-style:italic;font-weight:700;
    color:var(--red);font-size:23px;
  }
  .org{display:flex;justify-content:center;align-items:center;gap:12px;margin:8px 0 10px}
  .org .mark{width:22px;height:22px;border-radius:50%;background:var(--green)}
  .org .name{font-size:36px;line-height:1;color:var(--green);text-align:left}
  .url{
    font-family:"Roboto",sans-serif;font-style:italic;font-weight:900;
    color:var(--red);font-size:19px;letter-spacing:.5px;
  }
</style>
</head>
<body>

  <section class="banner banner-prepare">
    <div class="red-block hook">
      <span class="small">YOU DO NOT HAVE</span>
      <span class="small">TO LIVE IN A</span>
      <span class="big hl">FOREST</span>
      <span class="small">TO BE IN A</span>
      <span class="big wild hl">WILDFIRE!</span>
    </div>
    <div class="scene-art" role="img" aria-label="Illustration of a burning forest with embers arcing toward houses"></div>
    <div class="red-block call">
      <span>PREPARE</span>
      <span>NOW!</span>
    </div>
    <div class="choices">
      <span class="pill">YOUR HOME...</span>
      <span class="pill loss">YOUR LOSS...</span>
      <span class="pill">YOUR CHOICE!</span>
    </div>
    <div class="footer">
      <p class="learn">Learn more at</p>
      <div class="org"><span class="mark"></span><span class="name">EMBERGUARD<br>LARKTON</span></div>
      <p class="url">WWW.VREWC.ORG</p>
    </div>
  </section>

  <section class="banner banner-protect">
    <div class="red-block promise">
      <span class="line">The best way to</span>
      <span class="line">keep your</span>
      <span class="key hl">HOME <small>from</small></span>
      <span class="key hl">BURNING <small>is</small></span>
      <span class="line">to keep it from</span>
      <span class="key hl">CATCHING FIRE</span>
      <span class="line">in the first place.</span>
    </div>
    <div class="home-art" role="img" aria-label="Silhouette of houses and pine trees beneath red wildfire flames"></div>
    <p class="advice">PROTECT YOUR<br>HOME FROM WILDFIRE<br>CREATE IGNITION<br>RESISTANT SPACE</p>
    <div class="footer">
      <p class="learn">Learn more at</p>
      <div class="org"><span class="mark"></span><span class="name">EMBERGUARD<br>LARKTON</span></div>
      <p class="url">WWW.VREWC.ORG</p>
    </div>
  </section>

</body>
</html>
```